Special release wine label

Marrow Creek Cellars is a small premium wine producer in the Barossa - South Australia. We are a five star rated winery, producing exceptional wines true to variety, region and house style. We have a very special parcel of wine that we wish to release as an exclusive wine. Visit www.marrowcreekcellars.com.au for further feel.

The wine will be called Marrow Creek Cellars, 2012, The Amber Reserve Shiraz - Cabernet.

The wine can be bottled in either a burgundy or Bordeaux shaped bottle

```html
<!DOCTYPE html>
<html lang="en">
<head>
<meta charset="utf-8">
<title>Marrow Creek Cellars – The Amber Reserve 2012</title>
<link rel="stylesheet" href="https://fonts.googleapis.com/css2?family=Montserrat:wght@300;400&family=Libre+Caslon+Text&display=swap">
<style>
  :root {
    --paper: #ffffff;
    --frame: #ebebeb;
    --ink: #111111;
    --gold: #c8952e;
    --wine-red: #b8323a;
    --vignette: #e9e9e9;
    --vignette-deep: #bdbdbd;
  }
  html, body {
    margin: 0;
    padding: 0;
    width: 720px;
    height: 1200px;
    overflow: hidden;
    background: var(--paper);
  }
  .label {
    position: relative;
    width: 720px;
    height: 1200px;
    font-family: "Montserrat", "Helvetica Neue", Arial, sans-serif;
    color: var(--ink);
  }
  .label__frame {
    position: absolute;
    left: 51px;
    top: 50px;
    width: 602px;
    height: 1071px;
    border: 3px solid var(--frame);
  }
  .label__brand {
    position: absolute;
    top: 218px;
    left: 0;
    width: 720px;
    margin: 0;
    text-align: center;
    font-weight: 300;
    font-size: 41px;
    line-height: 52px;
    letter-spacing: 0.36em;
    text-indent: 0.36em;
    text-transform: uppercase;
  }
  .label__vintage {
    position: absolute;
    top: 336px;
    left: 0;
    width: 720px;
    text-align: center;
    font-weight: 300;
    font-size: 27px;
    letter-spacing: 0.3em;
    text-indent: 0.3em;
    color: var(--gold);
  }
  .label__vignette {
    position: absolute;
    left: 186px;
    top: 436px;
    width: 328px;
    height: 328px;
    border-radius: 50%;
    background: radial-gradient(circle at 50% 60%, var(--vignette-deep) 0%, #d4d4d4 35%, var(--vignette) 70%);
  }
  .label__wine {
    position: absolute;
    top: 838px;
    left: 0;
    width: 720px;
    text-align: center;
    font-weight: 400;
    font-size: 25px;
    line-height: 32px;
  }
  .label__wine p { margin: 0; }
  .label__region {
    position: absolute;
    top: 926px;
    left: 0;
    width: 720px;
    text-align: center;
    font-family: "Libre Caslon Text", Georgia, serif;
    font-size: 26px;
    color: var(--wine-red);
  }
</style>
</head>
<body>
  <main class="label">
    <div class="label__frame"></div>
    <h1 class="label__brand">Marrow Creek<br>Cellars</h1>
    <div class="label__vintage">2012</div>
    <div class="label__vignette" role="img" aria-label="Pencil sketch of the cellar homestead framed by tall palm trees"></div>
    <div class="label__wine">
      <p class="label__wine-name">The Amber Reserve</p>
      <p class="label__varietal">Shiraz - Cabernet</p>
    </div>
    <div class="label__region">South Australia</div>
  </main>
</body>
</html>
```